DeskWizard.dk Frontpage design

I'm in the process of starting a It-course website, based in Denmark. The web site Url is - www.deskwizard.dk

The services are:
- Online courses (This is the main service and the most important)
- One to One courses
- Webinar

I need a frontpage design a simple design, but it must shows professionalism. I have no preference in color, but I like white space.

In Denmark the established competitors are:
- www.tasniva.dk (Biggest competitor)
- www.bramfeldt.dk/online-kurser
- www.velunda.dk

Target Market(s)

Mainly companies (B to B), but there are also a small number of private customers

Industry/Entity Type

Online it courses and one to one consulting

Number of Pages Required

1 page

Font styles to use
Sans Serif

Requirements
Must have
• A professional design, white space

```html
<!DOCTYPE html>
<html lang="da">
<head>
<meta charset="utf-8">
<title>DeskWizard – Forside</title>
<link href="https://fonts.googleapis.com/css2?family=Outfit:wght@300;400;500;600;700&display=swap" rel="stylesheet">
<style>
:root{
  --teal:#00b39c;
  --teal-dark:#009e89;
  --mint:#e3f6f2;
  --ink:#15172b;
  --body:#5d6173;
  --muted:#9a9dab;
  --green-tag:#4bb567;
  --pink-tag:#d2507a;
  --purple-tag:#7a6fc9;
  --orange-tag:#e7a53a;
  --white:#ffffff;
}
*{box-sizing:border-box;margin:0;padding:0}
html,body{width:1200px;height:4167px;overflow:hidden}
body{font-family:"Outfit",sans-serif;color:var(--ink);background:var(--white);position:relative}
.abs{position:absolute}
a{color:inherit;text-decoration:none}

/* hero */
.hero{left:0;top:0;width:1200px;height:720px;overflow:hidden}
.hero-photo{position:absolute;inset:0;background:linear-gradient(120deg,#3b4a55 0%,#6c7a80 35%,#4a4a46 65%,#2d3336 100%)}
.hero-shade{position:absolute;inset:0;background:rgba(10,14,20,.35)}
.hero-wave{position:absolute;left:0;bottom:0}
.logo{font-weight:600;font-size:27px;color:var(--white)}
.nav{top:36px;left:419px;display:flex;gap:32px;font-size:14px;color:var(--white)}
.login{left:964px;top:29px;width:98px;height:36px;background:#15161b;color:var(--white);font-size:14px;font-weight:600;display:flex;align-items:center;justify-content:center;border-radius:2px}
.hero-title{left:0;width:1200px;top:330px;text-align:center;font-size:58px;font-weight:600;line-height:1.12;color:var(--white)}
.btn{display:flex;align-items:center;justify-content:center;font-weight:600;font-size:16px;letter-spacing:.5px;border-radius:2px}
.btn-teal{background:var(--teal);color:var(--white)}
.btn-dark{background:#1b1d22;color:var(--white);gap:10px;font-weight:500;font-size:18px}

/* section heads */
.sec-title{left:0;width:1200px;text-align:center;font-size:32px;font-weight:600}
.sec-sub{left:0;width:1200px;text-align:center;font-size:13px;color:var(--body)}

/* course cards */
.course{width:307px}
.course .pic{height:189px;border-radius:2px}
.course .body{padding:0 17px}
.tags{font-size:13px;display:flex;align-items:center;gap:8px;margin-top:25px}
.dot{width:5px;height:5px;border-radius:50%;background:var(--ink)}
.t-green{color:var(--green-tag)} .t-pink{color:var(--pink-tag)} .t-purple{color:var(--purple-tag)} .t-orange{color:var(--orange-tag)}
.course h3{font-size:16px;font-weight:600;margin-top:13px}
.course p{font-size:12.5px;line-height:1.65;color:var(--body);margin-top:9px}
.price{font-size:12px;font-weight:600;color:var(--teal);text-align:right;padding-right:34px;margin-top:28px}

/* why */
.why{width:190px;text-align:center;margin-left:-95px}
.why svg{display:block;margin:0 auto}
.why h4{font-size:15px;font-weight:600;margin-top:18px;line-height:1.3}
.why p{font-size:13px;color:var(--body);line-height:1.5;margin-top:18px}

/* webinar */
.webinar{left:0;top:1915px;width:1200px;height:720px;overflow:hidden}
.webinar-title{top:95px;font-size:32px;color:var(--white)}
.webinar-sub{top:130px;color:#dff6f1;width:500px;left:350px;line-height:1.6}
.wbox{width:390px;height:124px;border:1px solid rgba(255,255,255,.45);border-radius:3px;padding:34px 44px 0 45px;font-size:12.5px;line-height:1.7;color:var(--white)}
.wicon{position:absolute;left:-6px;top:-20px;background:var(--teal);padding:2px}
.laptop{left:204px;top:2272px;width:821px;height:470px}
.screen-body{position:absolute;left:88px;top:0;width:645px;height:432px;background:#1c1d20;border-radius:18px 18px 0 0;padding:12px 12px 18px}
.screen{width:100%;height:100%;background:linear-gradient(135deg,#c9c3b8 0%,#8d7f70 50%,#d8d2c6 100%);border-radius:6px;position:relative}
.play{position:absolute;left:50%;top:50%;width:76px;height:76px;margin:-38px 0 0 -38px;border-radius:50%;background:rgba(255,255,255,.85);display:flex;align-items:center;justify-content:center}
.base{position:absolute;left:0;top:430px;width:821px;height:28px;background:linear-gradient(#e0e1e4,#9c9ea3);border-radius:0 0 60px 60px/0 0 24px 24px}
.base-notch{position:absolute;left:355px;top:0;width:110px;height:8px;background:#c2c4c8;border-radius:0 0 8px 8px}

/* blog */
.post{width:300px;border:1px solid #eceef2;border-radius:2px;background:var(--white)}
.post .pic{height:193px}
.post .body{padding:0 23px 20px}
.post h3{font-size:17.5px;font-weight:600;margin-top:13px;line-height:1.55}
.post p{font-size:12.5px;color:var(--body);line-height:1.6;margin-top:13px}
.date{display:flex;align-items:center;gap:6px;font-size:11px;color:var(--muted);margin-top:14px}

/* one to one */
.oto-title{left:239px;top:3565px;font-size:32px;font-weight:600}
.oto-text{left:239px;top:3630px;width:285px;font-size:13px;line-height:1.6;color:var(--body)}

/* footer */
.footer{left:0;top:3905px;width:1200px;height:262px}
.fcol{font-size:15px;color:var(--white);line-height:27px}
.social{width:32px;height:32px;border-radius:50%;border:1.5px solid rgba(255,255,255,.8);background:rgba(255,255,255,.12)}
.copy{left:121px;top:4124px;font-size:11px;color:#d8f3ee}
.copy u{color:var(--white)}
</style>
</head>
<body>

<!-- HERO -->
<section class="abs hero">
  <div class="hero-photo" role="img" aria-label="Smilende mand med headset foran en bærbar computer"></div>
  <div class="hero-shade"></div>
  <svg class="hero-wave" width="1200" height="80" viewBox="0 0 1200 80" preserveAspectRatio="none">
    <path d="M0 50 Q600 0 1200 32 L1200 80 L0 80Z" fill="var(--mint)"/>
    <path d="M0 70 Q600 10 1200 55 L1200 80 L0 80Z" fill="#fff"/>
  </svg>
</section>
<div class="abs logo" style="left:115px;top:28px">DeskWizard</div>
<nav class="abs nav"><a>Kurser</a><a>Webinar</a><a>En Til En</a><a>Spørgsmål</a><a>Blog</a><a>Om</a><a>Kontakt</a></nav>
<a class="abs login">Log På</a>
<h1 class="abs hero-title">Styrk dine it kundskaber med<br>“just-in-time” learning</h1>
<a class="abs btn btn-teal" style="left:438px;top:514px;width:155px;height:44px">KOM IGANG</a>
<a class="abs btn btn-dark" style="left:616px;top:514px;width:146px;height:44px">
  <svg width="14" height="16" viewBox="0 0 14 16"><path d="M1 1 L13 8 L1 15Z" fill="var(--teal)"/></svg>Se Video</a>

<!-- COURSES -->
<h2 class="abs sec-title" style="top:818px">Udvalgte Kurser</h2>
<p class="abs sec-sub" style="top:865px">Find dit næste online kursus her</p>

<article class="abs course" style="left:115px;top:909px">
  <div class="pic" role="img" aria-label="Bærbar computer med gul startskærm" style="background:linear-gradient(135deg,#3a3a38,#e8b917 45%,#f0c92a 70%,#d9d9d6)"></div>
  <div class="body">
    <div class="tags"><span class="t-green">DataLens</span></div>
    <h3>Norvex DataLens På Én Time</h3>
    <p>Er det muligt at lære Norvex DataLens på kun én time? Nok ikke, men jeg kan give dig en introduktion.</p>
    <div class="price">199 Kr.</div>
  </div>
</article>
<article class="abs course" style="left:446px;top:909px">
  <div class="pic" role="img" aria-label="Skærm med programkode" style="background:linear-gradient(135deg,#0f2a3a,#1e5f7a 45%,#0c1820)"></div>
  <div class="body">
    <div class="tags"><span class="t-pink">GridCalc</span><span class="dot"></span><span class="t-purple">Serpa</span></div>
    <h3>Serpa For GridCalc Brugere</h3>
    <p>Hvordan kommer du som GridCalc brugere i gang med at bruge Serpa</p>
    <div class="price">499 Kr.</div>
  </div>
</article>
<article class="abs course" style="left:778px;top:909px">
  <div class="pic" role="img" aria-label="Hænder på tastatur foran kodeskærm" style="background:linear-gradient(135deg,#2a3038,#5a6470 50%,#d5b77a 100%)"></div>
  <div class="body">
    <div class="tags"><span class="t-purple">Serpa</span></div>
    <h3>Kvanta Introduktion</h3>
    <p>Introduktion til Kvanta programmering.</p>
    <div class="price">499 Kr.</div>
  </div>
</article>

<!-- WHY -->
<h2 class="abs sec-title" style="top:1429px">Hvorfor DeskWizard?</h2>
<p class="abs sec-sub" style="top:1477px">Jeg har siden 1995 undervist rigtig mange glade kursister.</p>

<div class="abs why" style="left:222px;top:1545px">
  <svg width="50" height="40" viewBox="0 0 50 40" fill="none" stroke="var(--teal)" stroke-width="2"><circle cx="16" cy="22" r="13"/><path d="M19 16c-2-2-7-2-7 1s7 2 7 6-5 3-7 1M16 13v18"/><path d="M28 12h18M28 18h18M30 24h16M30 30h16" stroke-width="3"/></svg>
  <h4>God Økonomi</h4>
  <p>Prisen på et online kursus er lavere end et fysisk kursus</p>
</div>
<div class="abs why" style="left:461px;top:1545px">
  <svg width="44" height="40" viewBox="0 0 44 40" fill="var(--teal)"><rect x="4" y="24" width="7" height="14"/><rect x="15" y="18" width="7" height="20"/><rect x="26" y="22" width="7" height="16"/><path d="M3 18 L16 9 L24 14 L38 3" fill="none" stroke="var(--teal)" stroke-width="3"/><circle cx="36" cy="13" r="6"/></svg>
  <h4>Hvorfor Vente</h4>
  <p>Styrk dine kompetencer på et online kursus nu</p>
</div>
<div class="abs why" style="left:705px;top:1545px">
  <svg width="44" height="42" viewBox="0 0 44 42" fill="none" stroke="var(--teal)" stroke-width="2"><circle cx="22" cy="12" r="9"/><path d="M22 7v5l4 2"/><path d="M3 22v10l9 8h6v-8l-6-7M41 22v10l-9 8h-6v-8l6-7"/></svg>
  <h4>Ingen Rejsetid</h4>
  <p>Du slipper for spildtid og bestemmer selv hvad du skal have til frokost</p>
</div>
<div class="abs why" style="left:949px;top:1545px">
  <svg width="44" height="40" viewBox="0 0 44 40" fill="none" stroke="var(--teal)" stroke-width="2.5"><rect x="3" y="3" width="38" height="34"/><path d="M3 10h38"/><path d="M13 30v-6M20 30v-10M27 30v-8M33 30v-14" stroke-width="4"/></svg>
  <h4>Designed In A<br>Browser</h4>
  <p style="margin-top:16px">Designing in a browser allows rapid development and saves cost.</p>
</div>
<a class="abs btn btn-teal" style="left:558px;top:1759px;width:84px;height:46px">OM</a>

<!-- WEBINAR -->
<section class="abs webinar">
  <svg width="1200" height="720" viewBox="0 0 1200 720" class="abs" style="left:0;top:0">
    <path d="M0 0H1200V560 Q900 520 600 540 Q300 560 0 655Z" fill="var(--teal)"/>
    <path d="M0 655 Q300 560 600 540 Q900 520 1200 560 V610 Q900 570 600 590 Q300 610 0 690Z" fill="var(--mint)"/>
  </svg>
  <h2 class="abs sec-title webinar-title">Webinar</h2>
  <p class="abs sec-sub webinar-sub">Jeg har siden 1995 Det er ikke kun på prisen at webinarer slår traditionelle kurser! rigtig mange glade kursister.</p>
  <div class="abs wbox" style="left:197px;top:189px">
    <svg class="wicon" width="42" height="32" viewBox="0 0 42 32" fill="none" stroke="#fff" stroke-width="2"><rect x="3" y="3" width="36" height="26" rx="4"/><path d="M17 10l10 6-10 6z"/></svg>
    Du får den sammen høje kvalitet på et webinar som på et traditionelt kursus, endda med den fordel at du kan se de igen og igen.
  </div>
  <div class="abs wbox" style="left:614px;top:189px">
    <svg class="wicon" width="42" height="36" viewBox="0 0 42 36" fill="none" stroke="#fff" stroke-width="2"><path d="M4 18L21 3l17 15M9 14v19h24V14M17 33V22h8v11"/></svg>
    Det bedste af det hele er du ikke behøver at flytte dig for at få ny viden
  </div>
</section>
<div class="abs laptop">
  <div class="screen-body">
    <div class="screen" role="img" aria-label="Videoramme: underviser med skriveplade foran en tavle">
      <div class="play"><svg width="26" height="28" viewBox="0 0 26 28"><path d="M3 2L24 14L3 26Z" fill="var(--teal)"/></svg></div>
    </div>
  </div>
  <div class="base"><div class="base-notch"></div></div>
</div>

<!-- BLOG -->
<h2 class="abs sec-title" style="top:2842px">Seneste Blogindlæg</h2>

<article class="abs post" style="left:120px;top:2920px">
  <div class="pic" role="img" aria-label="Regneark med løbende totaler" style="background:linear-gradient(180deg,#e6e8ee 0%,#4a72c4 18%,#d9e4f5 35%,#dde7f6 100%)"></div>
  <div class="body">
    <div class="tags"><span class="t-pink">GridCalc</span></div>
    <h3>Løbende Sum</h3>
    <p>Oprettelse Af Løbende Totaler</p>
    <div class="date"><svg width="11" height="11" viewBox="0 0 11 11" fill="none" stroke="currentColor"><rect x="1" y="2" width="9" height="8"/><path d="M1 4.5h9M3.5 1v2M7.5 1v2"/></svg>July 04, 2022</div>
  </div>
</article>
<article class="abs post" style="left:451px;top:2920px">
  <div class="pic" role="img" aria-label="Skærmbillede af datamenu i regneark" style="background:linear-gradient(180deg,#f4f4f4,#e9ece9 60%,#f7f7f7)"></div>
  <div class="body">
    <div class="tags"><span class="t-green">DataLens</span><span class="dot"></span><span class="t-pink">GridCalc</span></div>
    <h3>Brug DataLens Data I GridCalc</h3>
    <p>Norvex DataLens Er Et Super Program Til At At Analysere, Vise Og Dele Dine Rapport - Men Hvad Nu Hvis Du Gerne Vil Analysere Yderlige På Data I GridCalc?</p>
    <div class="date"><svg width="11" height="11" viewBox="0 0 11 11" fill="none" stroke="currentColor"><rect x="1" y="2" width="9" height="8"/><path d="M1 4.5h9M3.5 1v2M7.5 1v2"/></svg>June 17, 2022</div>
  </div>
</article>
<article class="abs post" style="left:781px;top:2920px">
  <div class="pic" role="img" aria-label="Skærmbillede af eksportmenu og linjediagram" style="background:linear-gradient(180deg,#f2f3f5,#ffffff 55%,#d4e3f8 100%)"></div>
  <div class="body">
    <div class="tags"><span class="t-green">DataLens</span><span class="dot"></span><span class="t-orange">SlideForge</span></div>
    <h3>Data Fra DataLens I SlideForge - Interaktivt</h3>
    <p>Nu Kan Du Præsentere Dine DataLens Data Direkte I SlideForge</p>
    <div class="date"><svg width="11" height="11" viewBox="0 0 11 11" fill="none" stroke="currentColor"><rect x="1" y="2" width="9" height="8"/><path d="M1 4.5h9M3.5 1v2M7.5 1v2"/></svg>June 14, 2022</div>
  </div>
</article>

<!-- ONE TO ONE -->
<h2 class="abs oto-title">En Til En</h2>
<p class="abs oto-text">Målrettet undervisning på det helt rigtige tidspunkt vil gøre dig bedre og hurtigere til dine opgaver</p>
<a class="abs btn btn-teal" style="left:238px;top:3714px;width:137px;height:46px">EN TIL EN</a>
<div class="abs" role="img" aria-label="Smilende mand foran en tavle med sedler" style="left:739px;top:3490px;width:332px;height:232px;background:linear-gradient(135deg,#e9ece9,#b9c4c6 50%,#2a3a4c)"></div>
<div class="abs" role="img" aria-label="Kvinde der arbejder ved en bærbar computer" style="left:636px;top:3677px;width:281px;height:178px;background:linear-gradient(135deg,#d9cbb7,#a98f72 45%,#2c3a55)"></div>

<!-- FOOTER -->
<footer class="abs footer">
  <svg width="1200" height="262" viewBox="0 0 1200 262" class="abs" style="left:0;top:0">
    <path d="M0 262V120 Q0 0 130 0H1200V262Z" fill="var(--teal)"/>
  </svg>
  <div class="abs logo" style="left:121px;top:72px;font-size:30px">DeskWizard</div>
  <div class="abs fcol" style="left:529px;top:76px">Kurser<br>Webinar<br>En Til En<br>Spørgsmål</div>
  <div class="abs fcol" style="left:715px;top:76px">Blog<br>Om<br>Kontakt<br>Terms</div>
  <div class="abs fcol" style="left:897px;top:76px;font-weight:600">Følg Os</div>
  <div class="abs social" style="left:898px;top:126px"></div>
  <div class="abs social" style="left:946px;top:126px"></div>
  <div class="abs social" style="left:993px;top:126px"></div>
</footer>
<p class="abs copy">©Copyright 2022. <u>DeskWizard</u> All Rights Reserved</p>

</body>
</html>
```